Ledger Tide Pro Banner Ad campaign

We are the number 1 leading automated journal & analytics platform for active traders in the crypto space

We will be running banner ads on a specialist ad network and need HTML designs + a good strategy.

Some of our key selling points to consider including:

- The #1 automated journaling & analytics solution for Crypto Traders
- We save traders time (from manual data entry that can be automated by our journal trade import service)
- We help traders improve through detailed analytics feedback on their trading performance
- LTP has helped thousands of crypto traders improve performance
- 5,700+ traders are using LTP to save themselves hundreds of data entry hours per year
- Analyse your full trade history in a click!

I have attached an example mockup we came up with internally but we are not professionals. Use it as a guide to heavily improve upon in the context of general design quality, and 'sales-y' lingo to improve conversions

Have added a £100 1st place payment increase upon advice from a designer Should incentivise the best of the best to submit work

Target Market(s)

Active traders in the crypto derivatives space. Trading on the following exchanges:

- Travora.com
- Quellix.com
- Morvane.com
- ZQK.com

Font styles to use
Other font styles liked:
• Quicksand is our main font atm

Colors
3277b5
33a6d7
0792cd
85abd2
3276b5
85acd3
85cae6
86cae7

Requirements
Must have
• similar colour scheme from my example upload.

Check our main website for more: ledgertidepro.com

Although bare in mind, its a bit old and shitty. We are now working with specialists to improve, so feel free to have some creative freedom
Nice to have
• Nice clear custom icons to accompany text. And a rotation of 2 or 3 of the main selling points from the project description

```html
<!DOCTYPE html>
<html lang="en">
<head>
<meta charset="utf-8">
<title>Ledger Tide Pro – Banner</title>
<link rel="stylesheet" href="https://fonts.googleapis.com/css2?family=Oswald:wght@600&family=Poppins:wght@400;600&display=swap">
<style>
  :root {
    --navy-deep: #083a68;
    --navy: #0b4f88;
    --blue-mid: #0d66a6;
    --brand-blue: #0792cd;
    --sky: #33a6d7;
    --sky-bright: #1aa9e1;
    --headline: #12a0dc;
    --stat-blue: #0a7fc0;
    --white: #ffffff;
    --silver-light: #f4f4f4;
    --silver-dark: #bdbdbd;
    --ink: #2b2b2b;
    --cta-ink: #0b3c6b;
    --stage: #c6c6c6;
  }
  * { margin: 0; padding: 0; box-sizing: border-box; }
  html, body {
    width: 1200px; height: 1105px; overflow: hidden;
    background: var(--stage);
  }
  .banner {
    position: absolute; left: 70px; top: 92px;
    width: 1046px; height: 875px; overflow: hidden;
    background: linear-gradient(160deg, var(--navy-deep) 0%, var(--navy) 55%, var(--blue-mid) 100%);
    font-family: "Poppins", sans-serif; color: var(--white);
  }
  .banner-shapes { position: absolute; inset: 0; }
  .brand {
    position: absolute; left: 20px; top: 40px;
    display: flex; align-items: center; gap: 14px;
  }
  .brand-mark {
    width: 26px; height: 26px; border: 2px solid var(--white);
  }
  .brand-name {
    font-family: "Poppins", sans-serif; font-weight: 400;
    font-size: 50px; letter-spacing: 4px; line-height: 1;
  }
  .headline-rank {
    position: absolute; left: 16px; top: 134px;
    font-family: "Oswald", sans-serif; font-weight: 600;
    font-size: 132px; line-height: 1; color: var(--headline);
    letter-spacing: 1px;
  }
  .headline-sub {
    position: absolute; left: 19px; top: 264px;
    font-size: 35px; line-height: 43.6px; font-weight: 400;
  }
  .benefits { position: absolute; left: 20px; top: 420px; width: 620px; list-style: none; }
  .benefit { position: relative; padding-left: 36px; font-size: 20.5px; line-height: 24.8px; }
  .benefit::after {
    content: ""; display: block; width: 155px; height: 0;
    border-bottom: 2px dotted rgba(255,255,255,0.8);
    margin-top: 12px;
  }
  .benefit + .benefit { margin-top: 17px; }
  .benefit-icon {
    position: absolute; left: 0; top: 1px; width: 25px; height: 25px;
  }
  .cta {
    position: absolute; left: 19px; top: 760px; width: 436px; height: 74px;
  }
  .cta-label {
    position: absolute; left: 0; top: 12px; width: 416px; height: 60px;
    display: flex; align-items: center; justify-content: center;
    font-size: 21px; color: var(--cta-ink); letter-spacing: 0.3px;
  }
  .stat-figure {
    position: absolute; left: 612px; top: 512px; width: 400px; text-align: center;
    font-family: "Oswald", sans-serif; font-weight: 600;
    font-size: 132px; line-height: 1; color: var(--stat-blue);
  }
  .stat-caption {
    position: absolute; left: 641px; top: 663px; width: 340px; text-align: center;
    font-size: 21px; line-height: 26.6px; color: var(--ink);
  }
  .stat-caption strong { font-weight: 600; display: block; }
</style>
</head>
<body>
<div class="banner">
  <svg class="banner-shapes" width="1046" height="875" viewBox="0 0 1046 875">
    <defs>
      <linearGradient id="photo-tones" x1="0" y1="0" x2="1" y2="1">
        <stop offset="0" stop-color="#2a2c31"/>
        <stop offset="0.45" stop-color="#6d6248"/>
        <stop offset="0.7" stop-color="#a8936a"/>
        <stop offset="1" stop-color="#26282c"/>
      </linearGradient>
      <radialGradient id="silver" cx="0.5" cy="0.5" r="0.6">
        <stop offset="0" stop-color="#ffffff"/>
        <stop offset="0.6" stop-color="#e6e6e6"/>
        <stop offset="1" stop-color="#bfbfbf"/>
      </radialGradient>
    </defs>
    <polygon points="335,0 453,0 394,57" fill="#ffffff"/>
    <g role="img" aria-label="Photo of gold crypto coins resting on a computer chip">
      <polygon points="453,0 1046,0 1046,418 713,875 560,875 671,503 322,129" fill="url(#photo-tones)"/>
    </g>
    <polygon points="322,129 394,57 540,200 470,272" fill="#0a2e52" opacity="0.55"/>
    <polygon points="1046,418 713,875 1046,875" fill="var(--sky-bright)"/>
    <circle cx="811" cy="636" r="206" fill="var(--sky-bright)"/>
    <circle cx="811" cy="636" r="190" fill="url(#silver)"/>
  </svg>

  <div class="brand">
    <span class="brand-mark"></span>
    <span class="brand-name">LTP</span>
  </div>

  <div class="headline-rank">THE #1</div>
  <h1 class="headline-sub">automated journaling<br>&amp; analytics solution for<br>Crypto Traders</h1>

  <ul class="benefits">
    <li class="benefit">
      <svg class="benefit-icon" viewBox="0 0 26 26"><circle cx="13" cy="13" r="12" fill="var(--sky)" stroke="#fff" stroke-width="2"/><rect x="8" y="7" width="9" height="12" rx="1" fill="none" stroke="#fff" stroke-width="1.5"/><path d="M10 11h5M10 14h3" stroke="#fff" stroke-width="1.3"/><path d="M14 17l5-6" stroke="#fff" stroke-width="1.6"/></svg>
      We save traders time (from manual data entry that can be automated by our journal trade import service)
    </li>
    <li class="benefit">
      <svg class="benefit-icon" viewBox="0 0 26 26"><circle cx="13" cy="13" r="12" fill="var(--sky)" stroke="#fff" stroke-width="2"/><path d="M7 8v11h12" fill="none" stroke="#fff" stroke-width="1.4"/><path d="M9 16l3-3 2 2 4-5" fill="none" stroke="#fff" stroke-width="1.5"/></svg>
      We help traders improve through detailed analytics feedback on their trading performance
    </li>
    <li class="benefit">
      <svg class="benefit-icon" viewBox="0 0 26 26"><circle cx="13" cy="13" r="12" fill="var(--sky)" stroke="#fff" stroke-width="2"/><circle cx="13" cy="13" r="6.5" fill="none" stroke="#fff" stroke-width="1.6"/><circle cx="13" cy="13" r="2" fill="#fff"/></svg>
      LTP has helped thousands of crypto traders improve performance
    </li>
    <li class="benefit">
      <svg class="benefit-icon" viewBox="0 0 26 26"><circle cx="13" cy="13" r="12" fill="var(--sky)" stroke="#fff" stroke-width="2"/><path d="M11 9l8 5-3.5 1 2 3.5-1.6.9-2-3.5L11 18z" fill="#fff"/></svg>
      Analyse your full trade history in a click!
    </li>
  </ul>

  <div class="cta">
    <svg width="436" height="74" viewBox="0 0 436 74">
      <polygon points="62,12 412,12 370,72 0,72" fill="#ffffff"/>
      <polygon points="60,1 434,1 392,62 20,62" fill="none" stroke="var(--sky-bright)" stroke-width="2"/>
    </svg>
    <span class="cta-label">START YOUR FREE TRIAL NOW</span>
  </div>

  <div class="stat-figure">5,700+</div>
  <p class="stat-caption">traders are using LTP to save themselves hundreds of data entry <strong>hours per year</strong></p>
</div>
</body>
</html>
```